Online video and marketing company business cards

Need to get some new business cards designed to fit with our new logo. The cards should be professional, clean and simple.

Cards should have:

Name
Position
2 line address
telephone
mobile
email address
web address

We need to have our logo and if possible say what we do...
ONLINE FILM PRODUCTION & STRATEGY

Marketing

```html
<!DOCTYPE html>
<html lang="en">
<head>
<meta charset="utf-8">
<title>brightreel business cards</title>
<link href="https://fonts.googleapis.com/css2?family=Source+Sans+3:wght@400;600;700&display=swap" rel="stylesheet">
<style>
  :root {
    --navy: #0e4470;
    --sky: #6fa6c6;
    --paper: #ffffff;
    --ink: #3d4650;
    --rule: #c9cfd5;
    --backdrop: #e9ebee;
  }
  * { box-sizing: border-box; margin: 0; padding: 0; }
  html, body { width: 1200px; height: 720px; overflow: hidden; }
  body {
    background: var(--backdrop);
    font-family: "Source Sans 3", "Helvetica Neue", Arial, sans-serif;
    position: relative;
  }
  .card {
    position: absolute;
    width: 540px;
    height: 309px;
    border-radius: 3px;
    box-shadow: 0 6px 18px rgba(0,0,0,0.14);
    overflow: hidden;
  }
  /* Front */
  .card-front { left: 60px; top: 70px; background: var(--paper); }
  .front-accent {
    position: absolute; right: 0; top: 0;
    width: 290px; height: 96px;
    background: linear-gradient(180deg, var(--navy) 0%, var(--navy) 45%, var(--sky) 100%);
  }
  .holder { position: absolute; right: 26px; top: 12px; text-align: right; color: var(--paper); }
  .holder-name { font-weight: 700; font-size: 19px; line-height: 1.15; }
  .holder-title { font-size: 12px; line-height: 1.2; }
  .brand {
    position: absolute; left: 38px; top: 128px;
    display: flex; align-items: center; gap: 10px;
  }
  .brand-dot { width: 34px; height: 34px; border-radius: 50%; background: var(--navy); flex: none; }
  .brand-name { font-weight: 700; font-size: 44px; color: var(--navy); letter-spacing: -0.5px; line-height: 1; }
  .contacts {
    position: absolute; left: 40px; top: 222px;
    list-style: none; color: var(--ink); font-size: 13px; line-height: 17px;
  }
  .contacts li { display: flex; align-items: center; gap: 7px; }
  .contacts svg { width: 10px; height: 10px; fill: var(--navy); flex: none; }
  .divider { position: absolute; left: 205px; top: 222px; width: 1px; height: 66px; background: var(--rule); }
  .address {
    position: absolute; left: 220px; top: 222px;
    color: var(--ink); font-size: 13px; line-height: 17px;
  }
  /* Back */
  .card-back { left: 600px; top: 340px; background: var(--navy); color: var(--paper); text-align: center; }
  .back-brand { margin-top: 70px; display: flex; justify-content: center; align-items: center; gap: 12px; }
  .back-brand .brand-dot { width: 46px; height: 46px; background: var(--paper); }
  .back-brand .brand-name { color: var(--paper); font-size: 48px; }
  .tagline { margin-top: 44px; font-size: 19px; letter-spacing: 1.2px; }
  .web { margin-top: 8px; font-size: 17px; letter-spacing: 3px; }
</style>
</head>
<body>
  <section class="card card-front" aria-label="Business card front">
    <div class="front-accent" role="img" aria-label="Decorative corner accent in navy and light blue"></div>
    <div class="holder">
      <div class="holder-name">Your Name</div>
      <div class="holder-title">Title</div>
    </div>
    <div class="brand">
      <span class="brand-dot"></span>
      <span class="brand-name">brightreel</span>
    </div>
    <ul class="contacts">
      <li><svg viewBox="0 0 10 10"><path d="M2 0 L4 2 L3 3.5 Q4.5 6 6.5 7 L8 6 L10 8 L8 10 Q1 9 0 2 Z"/></svg>123-456-0789</li>
      <li><svg viewBox="0 0 10 10"><rect x="2" y="0" width="6" height="10" rx="1"/></svg>123-456-0789</li>
      <li><svg viewBox="0 0 10 10"><rect x="0" y="2" width="10" height="7" rx="1"/></svg>info@brightreel.com</li>
      <li><svg viewBox="0 0 10 10"><circle cx="5" cy="5" r="5"/></svg>www.brightreel.com</li>
    </ul>
    <div class="divider"></div>
    <div class="address">Street Name, City Name<br>State Zip Code</div>
  </section>

  <section class="card card-back" aria-label="Business card back">
    <div class="back-brand">
      <span class="brand-dot"></span>
      <span class="brand-name">brightreel</span>
    </div>
    <p class="tagline">Online Film Production &amp; Strategy</p>
    <p class="web">www.brightreel.com</p>
  </section>
</body>
</html>
```